Lumora Wellness Group Showcase & E-Commerce Shopfront

Take the New Design WordPress Website Showcase and turn it into a fully functioning E-Commerce Shopfront.

1. The Web design in WordPress is almost complete.

- Please add Product Category detail Pages
- Add relevant product visuals
- Add up-to-date text
- Add carousel feature on Showcase Landing Page
- Add smart navigation features

2. Develop the Showcase Web site with Woo E-Commerce Platform
integration

3. For Woo Commerce develop Shopping Basket capability and develop full product range visual list with pricing.

4. Adapt Enquire Now / Contact page to direct to email inbox

TIMING

1. Could we get the Website Go Live status with no e-commerce integration ASAP
2. Develop Woo Commerce pages in 7 days

Important File Source:
Obtain base files here:
http://fyl.ex/t-Kq8rNvBzLa

Let me know if any further questions

Many thanks
Best wishes
Dirk

```html
<!DOCTYPE html>
<html lang="en">
<head>
<meta charset="utf-8">
<title>Contact Us – Lumora Wellness Group</title>
<link rel="stylesheet" href="https://fonts.googleapis.com/css2?family=Libre+Franklin:wght@400;500;600;700&family=Poppins:wght@700;800&family=Montserrat:wght@400;500&display=swap">
<style>
:root{
  --green:#2f9a1f;
  --green-dark:#1d7a12;
  --navy:#1a2aa0;
  --blue-btn:#1c30b4;
  --ink:#141414;
  --white:#ffffff;
  --field-border:#a9b7e6;
  --field-fill:#f1f4fd;
  --map:#e9ebe7;
}
*{box-sizing:border-box;margin:0;padding:0}
html,body{width:1200px;height:2772px;overflow:hidden;background:var(--white)}
body{font-family:"Libre Franklin",Arial,sans-serif;color:var(--navy)}
.canvas{position:relative;width:1200px;height:2772px;overflow:hidden}
.abs{position:absolute}

/* top bar */
.topbar{left:0;top:0;width:1200px;height:51px;background:var(--green)}
.topbar-contact{left:0;top:0;width:1200px;height:51px;display:flex;justify-content:center;align-items:center;gap:16px;color:var(--white);font-family:"Montserrat",sans-serif;font-size:18px;letter-spacing:2px}
.topbar-contact svg{vertical-align:-3px;margin-right:6px}
.enquire-btn{right:6px;top:6px;width:136px;height:38px;border-radius:19px;background:var(--blue-btn);color:var(--white);font-size:16px;display:flex;align-items:center;justify-content:center;box-shadow:0 3px 0 rgba(0,0,0,.25)}

/* header */
.brand-tab{left:125px;top:51px;width:188px;height:171px;background:var(--white);display:flex;align-items:center;justify-content:center}
.brand-name{font-family:"Libre Franklin",sans-serif;font-weight:600;font-size:40px;color:var(--green);line-height:1}
.main-nav{left:371px;top:94px;display:flex;gap:16px;font-weight:700;font-size:20px;color:var(--navy);align-items:center}

/* hero */
.hero-photo{left:0;top:168px;width:1200px;height:420px;background:radial-gradient(ellipse at 70% 30%,#c7e87a 0%,#8cc53a 35%,#4e9a1c 70%,#2f7a12 100%)}
.hero-title{left:443px;top:246px;width:314px;height:63px;background:var(--white);border-radius:8px;box-shadow:0 4px 10px rgba(0,0,0,.2);display:flex;align-items:center;justify-content:center;font-family:"Poppins",sans-serif;font-weight:800;font-size:44px;color:var(--green)}

/* info cards */
.info-card{top:571px;width:263px;height:321px;background:var(--white);border-radius:8px;box-shadow:0 10px 22px rgba(80,150,210,.35);text-align:center}
.info-icon{width:90px;height:90px;border-radius:50%;background:var(--green);margin:76px auto 0;display:flex;align-items:center;justify-content:center}
.info-title{margin-top:28px;font-family:"Poppins",sans-serif;font-weight:800;font-size:23px;color:var(--green)}
.info-text{margin-top:12px;font-weight:600;font-size:17px;color:var(--navy)}

/* map */
.map-area{left:0;top:974px;width:1200px;height:478px;background:linear-gradient(90deg,#b9e2a4 0%,#d9ead0 18%,var(--map) 30%,var(--map) 100%)}

/* contact form */
.form-shell{left:98px;top:1511px;width:1003px;height:527px;background:var(--white);box-shadow:0 4px 16px rgba(0,0,0,.14)}
.form-side{left:98px;top:1511px;width:410px;height:527px;background:linear-gradient(135deg,var(--green-dark),var(--green) 60%,#3fae26);color:var(--white);text-align:center}
.side-mark{width:56px;height:56px;border-radius:50%;border:8px solid var(--white);margin:150px auto 0}
.side-heading{margin-top:16px;font-family:"Poppins",sans-serif;font-weight:800;font-size:44px;line-height:1}
.side-name{margin-top:18px;font-weight:700;font-size:28px}
.side-tag{font-size:28px;line-height:34px}
.form-title{left:542px;top:1528px;font-family:"Poppins",sans-serif;font-weight:800;font-size:27px;color:var(--navy)}
.field-label{font-size:15px;color:var(--navy)}
.field{background:linear-gradient(var(--white),var(--field-fill));border:1px solid var(--field-border)}
.category-box{left:543px;top:1728px;width:520px;height:55px;border:1px solid var(--field-border);display:grid;grid-template-columns:repeat(3,1fr);padding:5px 16px;font-size:15px;color:var(--navy)}
.category-box span::before{content:"";display:inline-block;width:12px;height:12px;border:1px solid var(--navy);margin-right:14px;vertical-align:-1px}
.submit-btn{left:540px;top:1969px;width:138px;height:51px;border-radius:26px;background:var(--blue-btn);color:var(--white);font-weight:700;font-size:18px;display:flex;align-items:center;justify-content:center;box-shadow:0 4px 4px rgba(0,0,0,.3)}

/* footer */
.footer-base{left:0;top:2240px;width:1200px;height:532px;background:var(--ink)}
.footer-brand{left:0;top:2290px;width:1200px;text-align:center;font-weight:600;font-size:52px;color:var(--green);line-height:1}
.city-row{left:0;width:1200px;display:flex;justify-content:center;gap:22px;color:var(--white);font-size:18px;font-weight:500}
.city-row i{font-style:normal;color:var(--green);font-size:12px;line-height:24px}
.head-office{left:0;top:2533px;width:1200px;text-align:center;font-size:19px;color:var(--white)}
.head-office b{color:var(--green);font-weight:400}
.footer-url{left:0;top:2572px;width:1200px;text-align:center;font-family:"Montserrat",sans-serif;font-size:19px;letter-spacing:2px;color:var(--green)}
.social-row{left:0;top:2622px;width:1200px;display:flex;justify-content:center;gap:22px}
.social-row span{width:52px;height:52px;border-radius:50%;background:var(--green)}
.copyright{left:0;top:2699px;width:1200px;text-align:center;color:var(--white);font-size:15px;font-weight:500}
</style>
</head>
<body>
<div class="canvas">

  <div class="abs topbar"></div>
  <div class="abs topbar-contact">
    <span><svg width="18" height="18" viewBox="0 0 24 24" fill="none" stroke="#fff" stroke-width="2"><path d="M5 3h4l2 5-2.5 1.5a11 11 0 0 0 6 6L16 13l5 2v4a2 2 0 0 1-2 2A17 17 0 0 1 3 5a2 2 0 0 1 2-2z"/></svg>0200 555 0147</span>
    <span>|</span>
    <span><svg width="20" height="14" viewBox="0 0 20 14" fill="none" stroke="#fff" stroke-width="1.6"><rect x="1" y="1" width="18" height="12"/><path d="M1 1l9 7 9-7"/></svg>info@lumorawellness.com</span>
  </div>
  <div class="abs enquire-btn">ENQUIRE NOW</div>

  <div class="abs hero-photo" role="img" aria-label="Close-up photograph of fresh green leaves in soft sunlight"></div>
  <svg class="abs" style="left:0;top:360px" width="1200" height="260" viewBox="0 0 1200 260">
    <path d="M0 240 C150 10 350 -20 560 60 C760 130 950 150 1060 110 C1130 80 1180 40 1200 0 L1200 260 L0 260 Z" fill="#fff"/>
    <path d="M0 200 C150 20 350 0 560 70 C760 135 950 150 1060 112 C1130 85 1180 45 1200 0 C1180 60 1130 100 1060 125 C950 165 760 150 560 88 C350 25 150 40 0 145 Z" fill="var(--green)"/>
  </svg>
  <div class="abs hero-title">Contact Us</div>

  <div class="abs brand-tab"><span class="brand-name">Lumora</span></div>
  <nav class="abs main-nav">
    <span>HOME</span><span>ABOUT US</span><span>OUR PRODUCTS</span><span>OUR BRANDS</span><span>MEDIA</span><span>CONTACT US</span>
    <svg width="24" height="24" viewBox="0 0 24 24" fill="none" stroke="#9aa0a8" stroke-width="2"><circle cx="10" cy="10" r="7"/><path d="M15 15l7 7"/></svg>
  </nav>

  <div class="abs info-card" style="left:136px">
    <div class="info-icon"><svg width="48" height="60" viewBox="0 0 24 30" fill="none" stroke="#fff" stroke-width="1.6"><path d="M12 29C4 19 2 15 2 11a10 10 0 0 1 20 0c0 4-2 8-10 18z"/><circle cx="12" cy="11" r="4"/></svg></div>
    <div class="info-title">ADDRESS</div>
    <div class="info-text">London LW4 2QT</div>
  </div>
  <div class="abs info-card" style="left:468px">
    <div class="info-icon"><svg width="52" height="52" viewBox="0 0 24 24" fill="none" stroke="#fff" stroke-width="1.4"><path d="M5 2h4l2 5-2.5 1.5a11 11 0 0 0 7 7L17 13l5 2v4a2 2 0 0 1-2 2A18 18 0 0 1 3 4a2 2 0 0 1 2-2z"/></svg></div>
    <div class="info-title">PHONE</div>
    <div class="info-text">0200 555 0147</div>
  </div>
  <div class="abs info-card" style="left:801px">
    <div class="info-icon"><svg width="60" height="40" viewBox="0 0 30 20" fill="none" stroke="#fff" stroke-width="1.6"><rect x="1" y="1" width="28" height="18" rx="1"/><path d="M1 1l14 11 14-11M1 19l10-9M29 19l-10-9"/></svg></div>
    <div class="info-title">EMAIL</div>
    <div class="info-text">info@lumorawellness.com</div>
  </div>

  <div class="abs map-area" role="img" aria-label="Street map showing the office location"></div>

  <div class="abs form-shell"></div>
  <div class="abs form-side">
    <div class="side-mark"></div>
    <div class="side-heading">GET IN TOUCH!</div>
    <div class="side-name">Lumora Wellness.</div>
    <div class="side-tag">For your health, protection<br>and wellbeing.</div>
  </div>
  <div class="abs form-title">Contact Lumora Wellness Today</div>

  <div class="abs field-label" style="left:543px;top:1568px">First Name</div>
  <div class="abs field" style="left:543px;top:1592px;width:240px;height:33px"></div>
  <div class="abs field-label" style="left:827px;top:1568px">Last Name</div>
  <div class="abs field" style="left:827px;top:1592px;width:236px;height:33px"></div>

  <div class="abs field-label" style="left:543px;top:1637px">Company Name</div>
  <div class="abs field" style="left:543px;top:1661px;width:240px;height:33px"></div>
  <div class="abs field-label" style="left:827px;top:1637px">Contact Email</div>
  <div class="abs field" style="left:827px;top:1661px;width:236px;height:33px"></div>

  <div class="abs field-label" style="left:543px;top:1704px">Product Categories</div>
  <div class="abs category-box">
    <span>Product One</span><span>Product Two</span><span>Product Three</span>
    <span>Product Four</span><span>Product Five</span><span>Product six</span>
  </div>

  <div class="abs field-label" style="left:543px;top:1792px">Contact No</div>
  <div class="abs field" style="left:543px;top:1816px;width:240px;height:34px"></div>
  <div class="abs field-label" style="left:827px;top:1792px">Products of Interest</div>
  <div class="abs field" style="left:827px;top:1816px;width:236px;height:34px"></div>

  <div class="abs field-label" style="left:543px;top:1857px">Enquiry</div>
  <div class="abs field" style="left:543px;top:1883px;width:520px;height:75px"></div>
  <div class="abs submit-btn">SUBMIT</div>

  <svg class="abs" style="left:0;top:2010px" width="1200" height="240" viewBox="0 0 1200 240">
    <path d="M0 110 C200 230 450 180 700 115 C880 70 1080 60 1200 180 L1200 240 L0 240 Z" fill="var(--ink)"/>
    <path d="M0 0 C40 120 250 215 520 175 C700 148 850 100 1000 90 C900 110 750 160 560 195 C300 240 80 180 0 90 Z" fill="var(--green)"/>
  </svg>
  <div class="abs footer-base"></div>
  <div class="abs footer-brand">Lumora</div>

  <div class="abs city-row" style="top:2440px">
    <span>London</span><i>●</i><span>Paris</span><i>●</i><span>Madrid</span><i>●</i><span>Lisbon</span><i>●</i><span>Rome</span><i>●</i><span>Athens</span><i>●</i><span>Berlin</span><i>●</i><span>Dublin</span><i>●</i><span>Edinburgh</span>
  </div>
  <div class="abs city-row" style="top:2469px">
    <span>Amsterdam</span><i>●</i><span>Bruxelles</span><i>●</i><span>Stockholm</span><i>●</i><span>Copenhagen</span><i>●</i><span>Helsinki</span><i>●</i><span>Dubai</span><i>●</i><span>Capetown</span><i>●</i><span>Johannesburg</span>
  </div>
  <div class="abs head-office"><b>Head Office : </b>London LW4 2QT</div>
  <div class="abs footer-url">www.LumoraWellnessGroup.com</div>
  <div class="abs social-row" role="img" aria-label="Social media links">
    <span></span><span></span><span></span><span></span><span></span>
  </div>
  <div class="abs copyright">Lumora Wellness Group &nbsp; | &nbsp; All Rights Reserved © 2020</div>

</div>
</body>
</html>
```